Cedar Lantern Letterhead

I just need letterhead for my integrative psychiatry business. I'm going to use this to do mailings to other doctors, as well as send letters to patients. Thank you

Business

```html
<!DOCTYPE html>
<html lang="en">
<head>
<meta charset="utf-8">
<title>Cedar Lantern Letterhead</title>
<link rel="stylesheet" href="https://fonts.googleapis.com/css2?family=PT+Sans:wght@400;700&display=swap">
<style>
  :root {
    --backdrop: #e9e9e9;
    --paper: #ffffff;
    --leaf-green: #3f7a30;
    --bark-brown: #7a4320;
    --mist: #eef0ec;
    --band-text: #ffffff;
  }
  html, body {
    margin: 0;
    width: 1200px;
    height: 856px;
    overflow: hidden;
    background: var(--backdrop);
    font-family: "PT Sans", sans-serif;
  }
  .letterhead {
    position: absolute;
    left: 317px;
    top: 28px;
    width: 566px;
    height: 800px;
    background: var(--paper);
    box-shadow: 0 2px 10px rgba(0,0,0,0.12);
    overflow: hidden;
  }
  .letterhead svg { position: absolute; inset: 0; display: block; }
  .brand {
    position: absolute;
    left: 44px;
    top: 52px;
    display: flex;
    align-items: center;
    gap: 10px;
  }
  .brand-dot {
    width: 30px;
    height: 30px;
    border-radius: 50%;
    background: var(--leaf-green);
  }
  .brand-name {
    font-size: 22px;
    font-weight: 400;
    color: var(--bark-brown);
    letter-spacing: 0.3px;
  }
  .footer-contact {
    position: absolute;
    left: 18px;
    bottom: 10px;
    color: var(--band-text);
    font-size: 9.5px;
    line-height: 1.5;
  }
  .contact-row { display: flex; gap: 12px; align-items: center; }
  .contact-item { display: inline-flex; align-items: center; gap: 4px; }
  .contact-item svg { position: static; width: 10px; height: 10px; }
  .tagline {
    position: absolute;
    right: 16px;
    bottom: 118px;
    color: var(--band-text);
    font-size: 9.5px;
    font-weight: 700;
    transform: rotate(-28deg);
    transform-origin: right bottom;
  }
  .corner-mark {
    position: absolute;
    right: 30px;
    top: 612px;
    width: 22px;
    height: 22px;
    border-radius: 50%;
    background: var(--leaf-green);
  }
</style>
</head>
<body>
  <main class="letterhead">
    <svg width="566" height="800" viewBox="0 0 566 800" aria-hidden="true">
      <circle class="faint-emblem" cx="250" cy="470" r="175" fill="var(--mist)"/>
      <path class="footer-band" d="M0,762 C170,752 320,725 430,672 C490,643 530,622 566,604 L566,800 L0,800 Z" fill="var(--leaf-green)"/>
      <path class="footer-swoosh" d="M0,756 C170,745 320,716 430,662 C490,633 530,612 566,592" fill="none" stroke="var(--bark-brown)" stroke-width="2.5"/>
    </svg>

    <div class="brand">
      <span class="brand-dot"></span>
      <span class="brand-name">Cedar Lantern</span>
    </div>

    <span class="corner-mark"></span>

    <p class="tagline">A Professional Medical Corporation</p>

    <div class="footer-contact">
      <div class="address">2870 Alder Crest Way, Suite 210, Fairbrook, CA 95012</div>
      <div class="contact-row">
        <span class="contact-item">
          <svg viewBox="0 0 10 10"><circle cx="5" cy="5" r="4.5" fill="none" stroke="#fff"/><path d="M3.3 2.8 L4.2 2.6 L4.6 3.8 L4 4.3 Q4.6 5.5 5.7 6 L6.2 5.4 L7.4 5.8 L7.2 6.7 Q5 7 3.3 2.8 Z" fill="#fff"/></svg>
          555-014-2206
        </span>
        <span class="contact-item">
          <svg viewBox="0 0 10 10"><rect x="1" y="4" width="8" height="4.5" fill="#fff"/><rect x="2.5" y="1.5" width="5" height="3" fill="none" stroke="#fff"/></svg>
          555-014-2207
        </span>
        <span class="contact-item">
          <svg viewBox="0 0 10 10"><circle cx="5" cy="5" r="4.3" fill="none" stroke="#fff"/><ellipse cx="5" cy="5" rx="1.8" ry="4.3" fill="none" stroke="#fff" stroke-width="0.8"/><line x1="0.7" y1="5" x2="9.3" y2="5" stroke="#fff" stroke-width="0.8"/></svg>
          www.cedarlanternhealth.com
        </span>
      </div>
    </div>
  </main>
</body>
</html>
```